Need Letterhead and Business Card

I have a logo but i need new letterhead and biz cards. We are a real estate investment firm so we need very professional but also do not want to be old fashioned. We have 3 locations; Singapore, New York and Ponte Vedra Florida. I can provide full addresses if needed. If you have adjustments to our logo you would recommend we are open to them.
I will be putting in a separate project but we also need a template for our own powerpoint slide presentations and website.

Industry/Entity Type

Real Estate

```html
<!DOCTYPE html>
<html lang="en">
<head>
<meta charset="utf-8">
<title>Haven Business Card</title>
<link rel="stylesheet" href="https://fonts.googleapis.com/css2?family=Open+Sans:wght@400;600&display=swap">
<style>
  :root {
    --navy: #264d7e;
    --navy-text: #2a4f86;
    --gold: #c9a23a;
    --ink: #2b2b2b;
    --paper: #ffffff;
    --surface: #e5e6e8;
  }
  * { box-sizing: border-box; margin: 0; padding: 0; }
  html, body { width: 1200px; height: 794px; overflow: hidden; }
  body {
    background: var(--surface);
    font-family: "Open Sans", Arial, sans-serif;
    position: relative;
  }
  .card {
    position: absolute;
    top: 242px;
    width: 540px;
    height: 310px;
    border-radius: 3px;
    box-shadow: 0 2px 6px rgba(0,0,0,0.12);
  }
  .card-back { left: 40px; background: var(--navy); }
  .card-front { left: 620px; background: var(--paper); }

  .brand { position: absolute; }
  .brand-name {
    font-weight: 600;
    letter-spacing: 2px;
    line-height: 1;
  }
  .brand-rule { height: 1.5px; margin-top: 6px; }
  .brand-tagline {
    font-size: 10.5px;
    letter-spacing: 0.6px;
    text-transform: uppercase;
    color: var(--gold);
    margin-top: 4px;
  }
  .card-back .brand { left: 50%; top: 104px; transform: translateX(-50%); text-align: center; }
  .card-back .brand-name { font-size: 64px; color: var(--paper); }
  .card-back .brand-rule { background: var(--paper); }

  .card-front .brand { left: 36px; top: 70px; }
  .card-front .brand-name { font-size: 52px; color: var(--navy-text); }
  .card-front .brand-rule { background: var(--navy-text); }
  .card-front .brand-tagline { font-size: 9px; }

  .holder { position: absolute; left: 300px; top: 66px; }
  .holder-name { font-size: 17px; color: var(--ink); letter-spacing: 0.5px; }
  .holder-title { font-size: 12px; color: var(--ink); margin-top: 2px; }

  .divider {
    position: absolute; left: 36px; right: 36px; top: 172px;
    height: 1.5px; background: var(--gold);
  }

  .contact {
    position: absolute; left: 36px; top: 194px;
    font-size: 12.5px; color: var(--ink); line-height: 1.55;
    list-style: none;
  }
  .contact-label {
    display: inline-block; width: 16px;
    font-weight: 600; color: var(--navy-text);
  }
  .address {
    position: absolute; left: 300px; top: 194px;
    font-size: 12px; color: var(--ink); line-height: 1.5; font-style: normal;
  }
  .address .web { color: var(--navy-text); }
</style>
</head>
<body>
  <section class="card card-back" aria-label="Business card back">
    <div class="brand">
      <div class="brand-name">HAVEN</div>
      <div class="brand-rule"></div>
      <div class="brand-tagline">Real Estate Investment &amp; Management</div>
    </div>
  </section>

  <section class="card card-front" aria-label="Business card front">
    <div class="brand">
      <div class="brand-name">HAVEN</div>
      <div class="brand-rule"></div>
      <div class="brand-tagline">Real Estate Investment &amp; Management</div>
    </div>

    <div class="holder">
      <div class="holder-name">MARCO VELARDE</div>
      <div class="holder-title">Manager</div>
    </div>

    <div class="divider"></div>

    <ul class="contact">
      <li><span class="contact-label">T</span>(55) 5550 1427</li>
      <li><span class="contact-label">M</span>(55) 5550 3861</li>
      <li><span class="contact-label">E</span>marco.velarde@havenre.com</li>
    </ul>

    <address class="address">
      Calle Olmo 14. Col. Roma<br>
      Mexico City 06700. MX.<br>
      <span class="web">www.havenre.com</span>
    </address>
  </section>
</body>
</html>
```